Trulock Property Inspections

Property Inspection ( pre-purchase building inspections, swimming pool inspection, pest inspection , maintenance)

Industry/Entity Type

Building

Contact Information for Business Card

Omar Tanvelli
info@trulockinspections.com.au
0417 828 691

TruLock Property Inspections
www.trulockinspections.com.au

on the back

Property Inspections
Property Maintenance

Safe Home....Safe Familu

```html
<!DOCTYPE html>
<html lang="en">
<head>
<meta charset="utf-8">
<title>TruLock Property Inspections – Business Card</title>
<link href="https://fonts.googleapis.com/css2?family=Arimo:wght@400;700&display=swap" rel="stylesheet">
<style>
  :root {
    --page: #ffffff;
    --card-grey: #7e7778;
    --card-grey-light: #938c8d;
    --card-grey-dark: #6f6869;
    --swoosh: #4f4a4b;
    --panel: #f7f7f7;
    --brand-blue: #2a4fa8;
    --name-blue: #1b8fd1;
    --contact: #d6ecf7;
    --logo-ink: #1d1d1d;
  }
  html, body {
    margin: 0;
    width: 1200px;
    height: 1089px;
    overflow: hidden;
    background: var(--page);
    font-family: "Arimo", Arial, sans-serif;
  }
  .canvas {
    position: relative;
    width: 1200px;
    height: 1089px;
  }
  .card {
    position: absolute;
    left: 169px;
    width: 807px;
    height: 497px;
    overflow: hidden;
    background:
      radial-gradient(ellipse at 50% 30%, var(--card-grey-light) 0%, var(--card-grey) 55%, var(--card-grey-dark) 100%);
  }
  .card::before {
    content: "";
    position: absolute;
    inset: 0;
    background: repeating-linear-gradient(90deg,
      rgba(255,255,255,0.03) 0 14px,
      rgba(0,0,0,0.025) 14px 31px,
      rgba(255,255,255,0.015) 31px 52px);
  }
  .card--front { top: 25px; }
  .card--back { top: 558px; }

  .logo-diamond {
    position: absolute;
    left: 348px;
    top: 72px;
    width: 404px;
    height: 404px;
  }
  .logo-lockup {
    position: absolute;
    left: 348px;
    top: 72px;
    width: 404px;
    height: 404px;
    display: flex;
    flex-direction: column;
    align-items: center;
    justify-content: center;
    gap: 14px;
    text-align: center;
  }
  .logo-mark {
    width: 26px;
    height: 26px;
    background: var(--brand-blue);
  }
  .logo-name {
    margin: 0;
    width: 220px;
    font-size: 26px;
    line-height: 1.2;
    font-weight: 700;
    color: var(--brand-blue);
  }

  .back-art { position: absolute; inset: 0; }
  .holder-name {
    position: absolute;
    left: 469px;
    top: 200px;
    margin: 0;
    font-size: 37px;
    font-weight: 400;
    color: var(--name-blue);
    letter-spacing: 0.5px;
  }
  .contact {
    position: absolute;
    left: 49px;
    margin: 0;
    font-size: 28px;
    font-weight: 400;
    color: var(--contact);
    letter-spacing: 0.3px;
  }
  .contact--phone { top: 305px; }
  .contact--email { top: 367px; }
  .contact--web { top: 413px; }
</style>
</head>
<body>
<main class="canvas">
  <section class="card card--front" aria-label="Card front">
    <svg class="logo-diamond" viewBox="0 0 404 404" aria-hidden="true">
      <polygon points="202,0 404,202 202,404 0,202" fill="var(--panel)"/>
    </svg>
    <div class="logo-lockup">
      <span class="logo-mark" aria-hidden="true"></span>
      <p class="logo-name">TruLock Property Inspections</p>
    </div>
  </section>

  <section class="card card--back" aria-label="Card back">
    <svg class="back-art" viewBox="0 0 807 497" aria-hidden="true">
      <path class="name-panel" d="M290 136 L807 136 L807 330 L545 330 C470 300 390 250 330 205 C305 180 296 160 290 136 Z" fill="var(--panel)"/>
      <path class="swoosh" d="M197 -5 C240 90 250 160 330 220 S560 330 625 505" fill="none" stroke="var(--swoosh)" stroke-width="24" stroke-linecap="butt"/>
    </svg>
    <h1 class="holder-name">Omar Tanvelli</h1>
    <p class="contact contact--phone">0417 828 691</p>
    <p class="contact contact--email">info@trulockinspections.com.au</p>
    <p class="contact contact--web">www.trulockinspections.com.au</p>
  </section>
</main>
</body>
</html>
```